Painting services company needs a DL brochure about their services

We need a brochure describing our painting services including our logo and photos of work. The final design needs to be colourful, vibrant, and targeted to schools, aged care, commercial property maintenance clients.

```html
<!DOCTYPE html>
<html lang="en">
<head>
<meta charset="utf-8">
<title>Brightcoat Crew – DL Brochure</title>
<link href="https://fonts.googleapis.com/css2?family=Bebas+Neue&family=Open+Sans:wght@400;600;700&display=swap" rel="stylesheet">
<style>
  :root{
    --navy:#134a92;
    --navy-deep:#0d3a78;
    --yellow:#ffde17;
    --ink:#4a4a4a;
    --paper:#ffffff;
    --stage:#e9e9e9;
    --rule:#e6e8ec;
  }
  *{box-sizing:border-box;margin:0;padding:0}
  html,body{width:1200px;height:1122px;overflow:hidden;background:var(--stage)}
  body{position:relative;font-family:"Open Sans",Arial,sans-serif}
  .brochure{
    position:absolute;top:93px;width:393px;height:826px;background:var(--paper);
    transform:scale(1.1323);transform-origin:top left;overflow:hidden;
    box-shadow:0 2px 8px rgba(0,0,0,.12);
  }
  .brochure--services{left:120px}
  .brochure--sectors{left:635px}
  .hero-photo{position:absolute;left:0;top:0;width:393px;height:400px}
  .brochure--services .hero-photo{background:linear-gradient(180deg,#d9dadc 0%,#bfc0c2 45%,#7d7f82 80%,#5c5e61 100%)}
  .brochure--sectors .hero-photo{background:linear-gradient(160deg,#9fc4e6 0%,#d7d9dc 30%,#b9bcc0 60%,#8d9196 100%)}
  .wave{position:absolute;left:0;top:0;width:393px;height:826px}
  .brand{position:absolute;left:18px;top:236px;width:118px;height:164px;background:var(--paper);padding:14px 10px}
  .brand-square{display:block;width:40px;height:40px;background:var(--yellow);margin-bottom:12px}
  .brand-name{font-family:"Bebas Neue",Impact,sans-serif;color:var(--navy);font-size:34px;line-height:.95;letter-spacing:.5px}
  .title{position:absolute;left:158px;top:352px;font-family:"Bebas Neue",Impact,sans-serif;font-size:22px;line-height:1.08;letter-spacing:.3px}
  .title .line-1{color:var(--navy);display:block}
  .title .line-2{color:#f5c800;display:block}
  .lead{position:absolute;left:25px;top:424px;font-size:12.5px;font-weight:700;color:var(--navy);letter-spacing:-.1px}
  .intro{position:absolute;left:25px;top:446px;width:350px;font-size:11.6px;line-height:1.35;color:var(--ink)}
  .gallery{position:absolute;display:flex}
  .gallery .shot{height:100%}
  .brochure--services .gallery{left:25px;top:495px;width:351px;height:82px;gap:9px}
  .brochure--services .shot{width:111px}
  .brochure--sectors .gallery{left:15px;top:500px;width:363px;height:86px;gap:9px}
  .brochure--sectors .shot{width:115px}
  .shot--warehouse{background:linear-gradient(180deg,#6e7378,#3b3f43 55%,#8a8d90)}
  .shot--corridor{background:linear-gradient(180deg,#d8cbb8,#a98f72 60%,#7a6a58)}
  .shot--plant{background:linear-gradient(180deg,#9aa3ad,#6c5a4a 60%,#c9c3bb)}
  .shot--classroom{background:linear-gradient(180deg,#c9ccd0,#e8e9ea 55%,#8b8e92)}
  .shot--shopfront{background:linear-gradient(180deg,#2d5fb0,#f0c21a 60%,#8a8a8a)}
  .shot--factory{background:linear-gradient(180deg,#e27a3a,#6e7a86 50%,#c8ccd0)}
  .services-tab{position:absolute;left:0;top:598px;width:180px;height:30px;border-radius:0 15px 15px 0;
    background:linear-gradient(90deg,var(--navy-deep),var(--navy) 70%,#2a63b5);
    font-family:"Bebas Neue",Impact,sans-serif;color:var(--yellow);font-size:21px;line-height:31px;padding-left:26px}
  .service-list{position:absolute;top:634px;list-style:none}
  .service-list li{position:relative;padding-left:16px;height:22.8px;font-size:12px;color:#333;white-space:nowrap}
  .service-list li::before{content:"";position:absolute;left:0;top:5px;width:9px;height:9px;border-radius:50%;background:#f5c800}
  .service-list--a{left:30px}
  .service-list--b{left:190px}
  .quote-bar{position:absolute;left:0;top:756px;width:393px;height:34px;background:var(--navy);
    display:flex;align-items:center;padding-left:25px;gap:12px;font-family:"Bebas Neue",Impact,sans-serif;color:var(--yellow);font-size:22px}
  .quote-bar .phone{display:flex;align-items:center;gap:8px;margin-left:4px}
  .phone-icon{width:20px;height:20px}
  .web{position:absolute;font-size:11.5px;font-weight:700}
  .brochure--services .web{left:0;width:393px;top:796px;text-align:center;color:var(--navy)}
  .copy{position:absolute;left:15px;width:363px;font-size:10.9px;line-height:1.4;color:var(--ink);text-align:justify}
  .copy--sectors{top:425px}
  .copy--coatings{top:598px}
  .subhead{position:absolute;left:0;width:393px;top:662px;text-align:center;font-family:"Bebas Neue",Impact,sans-serif;font-size:22px;color:var(--navy)}
  .cta{position:absolute;left:15px;top:740px;font-family:"Bebas Neue",Impact,sans-serif;color:var(--yellow);font-size:22px;line-height:1.1}
  .cta .phone{display:flex;align-items:center;gap:8px}
  .brochure--sectors .web{left:15px;top:796px;color:#fff}
</style>
</head>
<body>

<section class="brochure brochure--services">
  <div class="hero-photo" role="img" aria-label="Photo of a restored heritage commercial building facade"></div>
  <svg class="wave" viewBox="0 0 393 826" aria-hidden="true">
    <path d="M0 290 C150 290 290 310 393 355 L393 826 L0 826 Z" fill="var(--yellow)"/>
    <path d="M0 294 C150 296 300 332 393 382 L393 826 L0 826 Z" fill="var(--paper)"/>
  </svg>
  <div class="brand"><span class="brand-square"></span><div class="brand-name">Brightcoat<br>Crew</div></div>
  <h1 class="title"><span class="line-1">Commercial Painting</span><span class="line-2">Contractor in Sydney</span></h1>
  <p class="lead">FAMILY-RUN BUSINESS WITH OVER 40 YEARS' EXPERIENCE</p>
  <p class="intro">We provide a full range of painting, decorating and protective coatings services through specialised divisions.</p>
  <div class="gallery">
    <div class="shot shot--warehouse" role="img" aria-label="Photo of a freshly painted warehouse interior"></div>
    <div class="shot shot--corridor" role="img" aria-label="Photo of a painted aged care corridor"></div>
    <div class="shot shot--plant" role="img" aria-label="Photo of coated industrial tanks and pipes"></div>
  </div>
  <h2 class="services-tab">Our Services</h2>
  <ul class="service-list service-list--a">
    <li>Residential painting</li>
    <li>Industrial painting</li>
    <li>Comercial painting</li>
    <li>Footpath restoration</li>
    <li>Epoxy floor coatings</li>
  </ul>
  <ul class="service-list service-list--b">
    <li>Coating to waterproof &amp; insulate</li>
    <li>Fascade restoration</li>
    <li>National retail branding</li>
    <li>Linemarking</li>
    <li>Painting of new buildings</li>
  </ul>
  <div class="quote-bar">
    <span>Call for a free quote!</span>
    <span class="phone">
      <svg class="phone-icon" viewBox="0 0 20 20" aria-hidden="true"><circle cx="10" cy="10" r="8.6" fill="none" stroke="var(--yellow)" stroke-width="1.8"/><path d="M7 5.5 L8.6 5.3 L9.4 7.8 L8.3 8.7 Q9.2 10.8 11.3 11.7 L12.2 10.6 L14.7 11.4 L14.5 13 Q13 14.7 10 13 Q6.5 11 5.8 8 Q5.5 6.3 7 5.5Z" fill="var(--yellow)"/></svg>
      1300 555 018
    </span>
  </div>
  <p class="web">www.brightcoatcrew.com.au</p>
</section>

<section class="brochure brochure--sectors">
  <div class="hero-photo" role="img" aria-label="Photo of a repainted white apartment tower with balconies"></div>
  <svg class="wave" viewBox="0 0 393 826" aria-hidden="true">
    <path d="M0 290 C150 290 290 310 393 355 L393 826 L0 826 Z" fill="var(--yellow)"/>
    <path d="M0 294 C150 296 300 332 393 382 L393 826 L0 826 Z" fill="var(--paper)"/>
    <path d="M0 645 C40 715 180 728 393 722 L393 826 L0 826 Z" fill="var(--yellow)"/>
    <path d="M0 665 C50 728 190 740 393 736 L393 826 L0 826 Z" fill="var(--navy)"/>
  </svg>
  <div class="brand"><span class="brand-square"></span><div class="brand-name">Brightcoat<br>Crew</div></div>
  <h1 class="title"><span class="line-1">Commercial Painting</span><span class="line-2">Contractor in Sydney</span></h1>
  <p class="copy copy--sectors">Our contractors transform nursing homes, schools, colleges, hospitals, retail shops, shopping centres, apartment blocks, townhouse developments, restaurants, warehouses and factories, offices, commercial premises and more.</p>
  <div class="gallery">
    <div class="shot shot--classroom" role="img" aria-label="Photo of a freshly painted school classroom"></div>
    <div class="shot shot--shopfront" role="img" aria-label="Photo of a painted retail shopfront"></div>
    <div class="shot shot--factory" role="img" aria-label="Photo of a painted factory floor"></div>
  </div>
  <p class="copy copy--coatings">Our commercial painters are qualified to apply texture coats from major painting brands, including Coatmaster Texra, and are experienced in all aspects of preparation and application of these speciality coatings.</p>
  <h2 class="subhead">Commercial Painting and Repainting</h2>
  <div class="cta">
    <div>Call for a free quote!</div>
    <div class="phone">
      <svg class="phone-icon" viewBox="0 0 20 20" aria-hidden="true"><circle cx="10" cy="10" r="8.6" fill="none" stroke="var(--yellow)" stroke-width="1.8"/><path d="M7 5.5 L8.6 5.3 L9.4 7.8 L8.3 8.7 Q9.2 10.8 11.3 11.7 L12.2 10.6 L14.7 11.4 L14.5 13 Q13 14.7 10 13 Q6.5 11 5.8 8 Q5.5 6.3 7 5.5Z" fill="var(--yellow)"/></svg>
      1300 555 018
    </div>
  </div>
  <p class="web">www.brightcoatcrew.com.au</p>
</section>

</body>
</html>
```